Halvern Drywork Business Card Design

Professional and clean design. The design colors should flow with the logo. Two-sided card with the website on the back which is:

www.HalvernDrywork.example.

"Specializing in Water Damage Restoration"

On the front I need the name, email, phone, and logo.

Name: Dorian Kettleby
Email: Dorian@HalvernDrywork.example
Phone: 555-0142-836 for now

I only have the Preview and Thumbnail right now but should have the source files uploaded within a day or two.

Target Market(s)

Flood victims, home owners with water damage from busted pipes etc...

Industry/Entity Type

Business

Contact Information for Business Card

Name: Dorian Kettleby

Font styles to use
Serif
Sans Serif

```html
<!DOCTYPE html>
<html lang="en">
<head>
<meta charset="utf-8">
<title>Halvern Drywork Business Card</title>
<link rel="stylesheet" href="https://fonts.googleapis.com/css2?family=Cinzel:wght@400&family=Source+Sans+3:wght@400;600&display=swap">
<style>
  :root {
    --stage: #161616;
    --card: #ffffff;
    --brand-blue: #1f8fd0;
    --brand-sky: #5bc4f0;
    --rule: #4fb4e6;
  }
  * { margin: 0; padding: 0; box-sizing: border-box; }
  html, body { width: 1200px; height: 741px; overflow: hidden; }
  body { background: var(--stage); position: relative; font-family: "Source Sans 3", sans-serif; }

  .card {
    position: absolute;
    top: 236px;
    height: 282px;
    background: var(--card);
    border-radius: 10px;
    overflow: hidden;
  }

  /* Back side */
  .card--back { left: 86px; width: 495px; }
  .back__badge {
    position: absolute; left: 217px; top: 52px;
    width: 62px; height: 62px; border-radius: 50%;
    background: var(--brand-sky);
  }
  .back__company {
    position: absolute; left: 0; right: 0; top: 124px;
    text-align: center;
    font-family: "Cinzel", serif; font-weight: 400;
    font-size: 33px; letter-spacing: 1px;
    color: var(--brand-blue);
  }
  .back__tagline {
    position: absolute; left: 0; right: 0; top: 181px;
    text-align: center;
    font-size: 13.5px; color: var(--brand-blue);
  }
  .back__web-row {
    position: absolute; left: 0; right: 0; top: 231px;
    display: flex; align-items: center; gap: 16px;
  }
  .back__web-row .rule { flex: 1; height: 1px; background: var(--rule); }
  .back__web { font-size: 13px; color: var(--brand-blue); }

  /* Front side */
  .card--front { left: 619px; width: 493px; }
  .front__brand {
    position: absolute; left: 24px; top: 56px; width: 172px;
    text-align: center;
  }
  .front__badge {
    width: 84px; height: 84px; border-radius: 50%;
    background: var(--brand-sky); margin: 0 auto 12px;
  }
  .front__company {
    font-family: "Cinzel", serif; font-weight: 400;
    font-size: 22px; line-height: 1.15;
    color: var(--brand-blue);
  }
  .front__divider {
    position: absolute; left: 217px; top: 60px;
    width: 1px; height: 162px; background: var(--rule);
  }
  .front__details { position: absolute; left: 232px; top: 64px; color: var(--brand-blue); }
  .front__name { font-size: 20px; font-weight: 600; }
  .front__phone { margin-top: 66px; font-size: 16px; }
  .contact-line { display: flex; align-items: center; gap: 5px; font-size: 14.5px; margin-top: 4px; }
  .contact-line:first-of-type { margin-top: 8px; }
  .contact-line svg { flex: none; }
</style>
</head>
<body>

  <section class="card card--back" aria-label="Card back">
    <div class="back__badge"></div>
    <h1 class="back__company">Halvern Drywork</h1>
    <p class="back__tagline">Specializing in Water Damage Restoration</p>
    <div class="back__web-row">
      <span class="rule"></span>
      <span class="back__web">www.HalvernDrywork.example</span>
      <span class="rule"></span>
    </div>
  </section>

  <section class="card card--front" aria-label="Card front">
    <div class="front__brand">
      <div class="front__badge"></div>
      <p class="front__company">Halvern<br>Drywork</p>
    </div>
    <div class="front__divider"></div>
    <div class="front__details">
      <h2 class="front__name">Dorian Kettleby</h2>
      <p class="front__phone">555-0142-836 for now</p>
      <p class="contact-line">
        <svg width="13" height="11" viewBox="0 0 13 11" aria-hidden="true">
          <rect x="0" y="0" width="13" height="11" rx="1.5" fill="var(--brand-sky)"/>
          <path d="M2 2.5 L6.5 6 L11 2.5" fill="none" stroke="#fff" stroke-width="1.2"/>
        </svg>
        Dorian@HalvernDrywork.example
      </p>
      <p class="contact-line">
        <svg width="13" height="13" viewBox="0 0 13 13" aria-hidden="true">
          <rect x="0" y="0" width="13" height="13" rx="1.5" fill="var(--brand-sky)"/>
          <circle cx="6.5" cy="6.5" r="4.3" fill="none" stroke="#fff" stroke-width="1"/>
          <ellipse cx="6.5" cy="6.5" rx="1.8" ry="4.3" fill="none" stroke="#fff" stroke-width="0.9"/>
          <line x1="2.2" y1="6.5" x2="10.8" y2="6.5" stroke="#fff" stroke-width="0.9"/>
        </svg>
        www.HalvernDrywork.example
      </p>
    </div>
  </section>

</body>
</html>
```